Shopping center investment profile

We need to design a two-page 8.5" x 11" brochure that can be used as a template for profiling our shopping centers and demonstrating our track record to investors.

Our company (KVM Real Estate Investments) owns retail shopping centers in the southwestern United States. Our website is www.kvmtrh.example, but we will be redesigning and modernizing the website and logo in the near future, so please do not use the color schemes or framework of the website for the brochure.

Our investors are institutional and high net worth investors who typically have an existing relationship with our company. They are determining whether to invest multi-millions of dollars in a shopping center opportunity, so the brochure needs to be professional, very high quality and provide key information about the specific property.
Updates

Additional guidance on color scheme:

We would like to see a Blue (something like Hex #5A61BC) and Gold (Hex #EDB215) or (Hex #DDA24B) color scheme with some Black accents 

Thank you!

Target Market(s)

Our target audiences are institutional investors, high net-worth individuals, financial firms and medium to large commercial real estate companies.

Industry/Entity Type

Investment

Requirements
Must have
• Clean and modern look with corresponding fonts and colors.
• Incorporates the information found in the attached "Marlowe Crossing profile" Pages or PDF file.
• Final file design files that can be modified easily
Nice to have
• Two examples of industry brochures are attached. These are examples of the professional quality that we are looking for, not necessarily the design or format.

```html
<!DOCTYPE html>
<html lang="en">
<head>
<meta charset="utf-8">
<title>Marlowe Crossing – Property Profile</title>
<link rel="stylesheet" href="https://fonts.googleapis.com/css2?family=Arimo:wght@400;700&family=Roboto+Condensed:wght@700&display=swap">
<style>
  :root{
    --blue:#5a5fb2;
    --gold:#edb215;
    --lavender:#d8d7ee;
    --ink:#231f20;
    --white:#ffffff;
    --navy:#33377f;
    --map:#e7e3da;
  }
  *{margin:0;padding:0;box-sizing:border-box}
  html,body{width:927px;height:1200px;overflow:hidden;background:var(--white)}
  .sheet{position:relative;width:927px;height:1200px;overflow:hidden;font-family:"Arimo",Helvetica,Arial,sans-serif;color:var(--ink)}
  .shapes{position:absolute;inset:0}
  .cond{font-family:"Roboto Condensed","Arial Narrow",sans-serif;font-weight:700}

  .company-name{font-family:"Arimo",Helvetica,Arial,sans-serif;font-weight:700;font-size:22px;line-height:27px}
  .brand-top{position:absolute;left:58px;top:44px;width:140px;color:var(--ink)}
  .brand-foot{position:absolute;left:30px;top:1000px;width:170px;color:var(--white)}

  .title{position:absolute;left:252px;top:38px;color:var(--white)}
  .title h1{font-size:51px;line-height:1;letter-spacing:.3px}
  .title p{font-size:25px;margin-top:8px}

  .tag{position:absolute;right:30px;top:30px;text-align:right;color:var(--navy);font-size:20px;line-height:24px}

  .caption{position:absolute;top:614px;left:260px;right:45px;height:35px;display:flex;justify-content:space-between;align-items:center;color:var(--white);font-size:19px}

  .summary{position:absolute;left:234px;top:700px;width:278px}
  h2{font-size:23px;color:var(--ink);margin-bottom:16px}
  .facts{width:100%;border-collapse:collapse;font-size:14px}
  .facts td{padding:6px 6px 4px;border-bottom:1.5px solid var(--ink);vertical-align:top;line-height:16px}
  .facts tr:first-child td{border-top:1.5px solid var(--ink)}
  .facts td.val{text-align:right}

  .opportunity{position:absolute;left:541px;top:703px;width:370px}
  .results{position:absolute;left:541px;top:950px;width:370px}
  .points{list-style:none;font-size:13.4px;line-height:16.4px}
  .points li{position:relative;padding-left:16px}
  .points li::before{content:"";position:absolute;left:0;top:5px;width:7px;height:7px;border-radius:50%;background:var(--ink)}

  .address{position:absolute;left:30px;top:1096px;color:var(--white);font-size:12px;line-height:15px;font-style:normal}
</style>
</head>
<body>
<div class="sheet">
  <svg class="shapes" width="927" height="1200" viewBox="0 0 927 1200">
    <polygon points="0,42 46,88 204,88 204,1200 0,1200" fill="var(--blue)"/>
    <rect x="211" y="649" width="716" height="551" fill="var(--lavender)"/>
    <rect x="211" y="0" width="716" height="160" fill="var(--blue)"/>
    <polygon points="728,0 927,0 927,160 922,160" fill="var(--white)"/>
    <polygon points="738,0 927,0 927,150" fill="var(--gold)"/>
    <rect x="46" y="0" width="158" height="160" fill="var(--gold)"/>
    <rect x="0" y="160" width="927" height="7" fill="var(--white)"/>
    <g role="img" aria-label="Street map of the area around the shopping center with a location pin">
      <polygon points="46,167 204,167 204,607 166,569 46,569" fill="var(--map)"/>
    </g>
    <polygon points="46,569 166,569 204,607 204,620 46,620" fill="var(--blue)"/>
    <rect x="204" y="160" width="7" height="1040" fill="var(--white)"/>
    <polygon points="204,607 215,607 256,649 245,649" fill="var(--white)"/>
    <defs>
      <linearGradient id="scene" x1="0" y1="0" x2="0" y2="1">
        <stop offset="0" stop-color="#3f86d0"/>
        <stop offset=".45" stop-color="#b9cde0"/>
        <stop offset=".6" stop-color="#c99a78"/>
        <stop offset=".8" stop-color="#7a5a4c"/>
        <stop offset="1" stop-color="#4a4a52"/>
      </linearGradient>
    </defs>
    <rect x="211" y="167" width="716" height="443" fill="url(#scene)" role="img" aria-label="Rendering of the shopping center storefronts with signage, trees and parking lot"/>
    <polygon points="219,614 927,614 927,649 254,649" fill="var(--ink)"/>
  </svg>

  <div class="brand-top company-name">KVM Real Estate Investments</div>

  <header class="title cond">
    <h1>Marlowe Crossing</h1>
    <p>Gilbert, Arizona</p>
  </header>
  <div class="tag cond">Property<br>Profile</div>

  <div class="caption cond"><span>Marlowe Crossing, Gilbert, Arizona</span><span>79.490 sq ft</span></div>

  <section class="summary">
    <h2 class="cond">Summa</h2>
    <table class="facts">
      <tr><td>Property Type</td><td class="val">Shopping Center</td></tr>
      <tr><td>Size</td><td class="val">79,490 sq ft</td></tr>
      <tr><td>79,490 sq ft</td><td class="val">April 2011</td></tr>
      <tr><td>Total Investment</td><td class="val">$X,XXX,XXX</td></tr>
      <tr><td>Purchase Occupancy</td><td class="val">8,39%</td></tr>
      <tr><td>Current Occupancy</td><td class="val">97,29%</td></tr>
      <tr><td>Projected 5-year IRR<br>(Unleveraged)</td><td class="val">XX.XX%</td></tr>
    </table>
  </section>

  <section class="opportunity">
    <h2 class="cond">Opportunity</h2>
    <ul class="points">
      <li>Bank owned property with attractive purchase price</li>
      <li>Strong relationship with seller’s broker<br>and decision makers</li>
      <li>Redevelopment upside with management and leasing</li>
      <li>No major renovations required</li>
      <li>Gilbert location has very strong population, education and income demographics</li>
      <li>Adjacent to premier 2,500-residence master planned community of Palo Verde Shores</li>
      <li>Strong employment area with the new Crestline Regional hospital and the adjacent Halvorsen Cancer center</li>
    </ul>
  </section>

  <section class="results">
    <h2 class="cond">Results</h2>
    <ul class="points">
      <li>Stabilized the shopping center within three years, producing excellent results for investors</li>
      <li>Transformed the center into a vibrant destination<br>that the surrounding community is excited about</li>
      <li>Transitioned legacy tenants to upgrade<br>the business operators</li>
      <li>Reduced the shopping center’s operating expenses by replacing vendors and appealing property taxes</li>
    </ul>
  </section>

  <div class="brand-foot company-name">KVM Real Estate Investments</div>
  <address class="address">4470 E Harmon Way Suite 210<br>Mesa, AZ 85206<br>(480) 555-0142</address>
</div>
</body>
</html>
```